Business Card and Stationary Design

After the successful redesign of our logo we are wanting to follow suite and create a new business card and stationary design!

New Logo is attached, information required on the business card should contain a mixture of the following but layout/arrangement is up to the designer.

Happy if the national provider number and abn are on the back, and happy for them to be smaller than the rest.

I am also happy to receive single sided or weird and wonderful designs.

Name
Title
National Provider Number 7291
ABN 53 219 864 317
Level 3, 42 Marlow Street
Kelvale NSW 2291
Ph: 1300 987 214
Mobile: 0432 785 619
name@ferngatebuild.com.au
www.ferngatebuild.com.au

Target Market(s)

Professionals, Peers, Students, Suppliers...

Industry/Entity Type

Construction

Contact Information for Business Card

Listed in project description

Font styles to use
Other font styles liked:
• Century Gothic

Colors
0455a3
3176b5
ffffff

Requirements
Must have
• Professional Design, same color scheme as our logo
Nice to have
• Something that sets our apart from everyone else would be fantastic, open to size and shape and layout options, as long as they present professionally.
• Open to raised/embossed text, alternative materials, custom sizes, clear material
Should not have
• The color orange

```html
<!DOCTYPE html>
<html lang="en">
<head>
<meta charset="utf-8">
<title>Ferngate Build – Business Card</title>
<link rel="stylesheet" href="https://fonts.googleapis.com/css2?family=Mulish:wght@400;600;700;800&family=Questrial&display=swap">
<style>
  :root {
    --navy: #1f3a7a;
    --navy-light: #2d4c8f;
    --brand-blue: #0455a3;
    --grey-text: #7a7a7a;
    --grey-strong: #6d6d6d;
    --white: #ffffff;
    --backdrop: #d9d9db;
  }
  * { box-sizing: border-box; margin: 0; padding: 0; }
  html, body {
    width: 1200px; height: 1000px; overflow: hidden;
    background: var(--backdrop);
    font-family: "Mulish", "Questrial", sans-serif;
  }
  .canvas { position: relative; width: 1200px; height: 1000px; }

  .card {
    position: absolute; left: 269px; width: 662px; height: 380px;
    box-shadow: 0 3px 8px rgba(0,0,0,0.35);
  }
  .card-front {
    top: 108px;
    background: linear-gradient(115deg, var(--navy) 0%, var(--navy) 35%, var(--navy-light) 55%, var(--navy) 100%);
  }
  .card-back { top: 520px; background: var(--white); }

  .front-decor {
    position: absolute; right: 0; top: 0; width: 440px; height: 380px;
    background: linear-gradient(90deg, rgba(255,255,255,0) 0%, rgba(255,255,255,0.05) 30%, rgba(255,255,255,0.07) 100%);
  }

  .wordmark {
    font-family: "Questrial", sans-serif;
    font-weight: 400; letter-spacing: 0.2px; line-height: 1;
    display: flex; align-items: center; gap: 10px;
  }
  .wordmark-square { width: 14px; height: 14px; }

  .card-front .wordmark {
    position: absolute; left: 17px; top: 12px;
    font-size: 34px; color: var(--white);
  }
  .card-front .wordmark-square { background: var(--white); }

  .card-back .wordmark {
    position: absolute; left: 35px; top: 40px;
    font-size: 30px; color: var(--navy);
  }
  .card-back .wordmark-square { background: var(--navy); }

  .person { position: absolute; left: 82px; top: 188px; }
  .person-name {
    font-weight: 800; font-size: 18px; letter-spacing: 0.5px;
    color: var(--navy); line-height: 22px;
  }
  .person-title { font-size: 15px; color: var(--grey-text); line-height: 20px; margin-top: 1px; }

  .contact-list { list-style: none; position: absolute; left: 82px; top: 247px; }
  .contact-item {
    display: flex; align-items: center; gap: 5px;
    font-size: 15px; line-height: 19.3px; color: var(--grey-text);
  }
  .contact-item svg { width: 12px; height: 12px; fill: var(--navy); flex: none; }

  .company-info {
    position: absolute; right: 38px; top: 234px; text-align: right;
    font-size: 15px; line-height: 19.5px; color: var(--grey-text);
  }
  .company-info strong { font-weight: 700; color: var(--grey-strong); }
  .company-address { margin-top: 13px; }
</style>
</head>
<body>
<div class="canvas">

  <section class="card card-front">
    <div class="front-decor" role="img" aria-label="Subtle tonal brand decoration in deep blue"></div>
    <div class="wordmark"><span class="wordmark-square"></span>ferngate build</div>
  </section>

  <section class="card card-back">
    <div class="wordmark"><span class="wordmark-square"></span>ferngate build</div>

    <div class="person">
      <p class="person-name">DANIEL HARPER</p>
      <p class="person-title">Managing Director</p>
    </div>

    <ul class="contact-list">
      <li class="contact-item">
        <svg viewBox="0 0 12 12" aria-hidden="true"><path d="M2.5 1l2 2.2-1 1.3c.7 1.5 1.6 2.4 3 3l1.3-1L10 8.5 8.8 11C5 10.6 1.4 7 1 3.2z"/></svg>
        1300 987 214
      </li>
      <li class="contact-item">
        <svg viewBox="0 0 12 12" aria-hidden="true"><path d="M3.5 0h5a1 1 0 0 1 1 1v10a1 1 0 0 1-1 1h-5a1 1 0 0 1-1-1V1a1 1 0 0 1 1-1zm.3 1.3v8.2h4.4V1.3zM6 10.2a.6.6 0 1 0 0 1.2.6.6 0 0 0 0-1.2z"/></svg>
        0432 785 619
      </li>
      <li class="contact-item">
        <svg viewBox="0 0 12 12" aria-hidden="true"><path d="M1 3h10v7H1zm1 1v.3l4 2.7 4-2.7V4zm0 1.5V9h8V5.5L6 8.2z"/></svg>
        name@ferngatebuild.com.au
      </li>
      <li class="contact-item">
        <svg viewBox="0 0 12 12" aria-hidden="true"><path d="M6 1a5 5 0 1 0 0 10A5 5 0 0 0 6 1zm0 1c.6 0 1.3 1.2 1.5 3h-3C4.7 3.2 5.4 2 6 2zM4.5 6h3c-.2 1.8-.9 3-1.5 3s-1.3-1.2-1.5-3zM2 5a4 4 0 0 1 1.8-2.4A6 6 0 0 0 3.5 5zm0 1h1.5a6 6 0 0 0 .3 2.4A4 4 0 0 1 2 6zm6.5-1a6 6 0 0 0-.3-2.4A4 4 0 0 1 10 5zm0 1H10a4 4 0 0 1-1.8 2.4A6 6 0 0 0 8.5 6z"/></svg>
        www.ferngatebuild.com.au
      </li>
    </ul>

    <div class="company-info">
      <p><strong>National Provider Number:</strong> 7291</p>
      <p><strong>ABN:</strong> 53 219 864 317</p>
      <div class="company-address">
        <p>Level 3, 42 Marlow Street</p>
        <p>Kelvale NSW 2291</p>
      </div>
    </div>
  </section>

</div>
</body>
</html>
```